Keep Climbing - Nobody Writes My Ending

The front book cover. The book will include life lessons I've learned through three breast cancer (Teal Lantern) diagnoses and how to create positivity through adversity. Lessons that most people don't think of until they're hit with a life-altering setback. The chapters include Imposter Syndrome (Teal Lantern Warriors don't have time to debate if they're good enough, they just jump in and get it done because life is too short), Stand Your Ground (stick up for your beliefs and advocate for yourself), The Flip Side of It's All About Me (like an emergency rescuer who must equip themselves first, you need to take care of yourself first). The main message in the book is when others say you CAN'T, I say you CAN! Warrior means being strong no matter what life deals you. I've included a word document with more information.

Please note: Pink is only to be an accent color. I'd like my brand colors to be included. The title of the book is to be the focus with an image to add to the book cover appeal.

Target Market(s)

professionals with a growth mindset and people going through adversity

Industry/Entity Type

HR, Libraries, Hosppitality,

Font styles to use
Sans Serif

Colors
6B429C
8869AF
B7A5CE
E3DAEB
F3F0F8

Requirements
Must have
• Be original. Cover to be appealing to male and female buyers. Incorporate my purple brand color. Be creative and unique.
Nice to have
• Although I have offered a suggestion, I'm open to a creative cover that wows me.
Should not have
• No cartoon image or stock image

```html
<!DOCTYPE html>
<html lang="en">
<head>
<meta charset="utf-8">
<title>Nobody Writes My Ending – Front Cover</title>
<link rel="stylesheet" href="https://fonts.googleapis.com/css2?family=Jost:wght@400&display=swap">
<style>
  :root {
    --backdrop: #262626;
    --paper: #ffffff;
    --plum-left: #633c79;
    --plum-right: #94229a;
    --gold-light: #e6c978;
    --gold-deep: #b48f3a;
    --gold-text: #b99848;
    --glove-light: #c45fd4;
    --glove-deep: #7a1a86;
  }
  * { margin: 0; padding: 0; box-sizing: border-box; }
  html, body { width: 1200px; height: 1200px; overflow: hidden; background: var(--backdrop); }
  .canvas { position: relative; width: 1200px; height: 1200px; }
  .cover {
    position: absolute; left: 236px; top: 17px; width: 728px; height: 1165px;
    background: var(--paper); overflow: hidden;
    font-family: "Jost", sans-serif;
  }
  .title-disc {
    position: absolute; left: -83px; top: -368px; width: 894px; height: 894px;
    border-radius: 50%;
    background: linear-gradient(90deg, var(--plum-left), var(--plum-right));
  }
  .title { position: absolute; left: 0; top: 0; width: 728px; text-align: center; }
  .title-line {
    position: absolute; left: 0; width: 100%;
    line-height: 1; font-weight: 400; text-transform: uppercase;
    background: linear-gradient(180deg, var(--gold-light), var(--gold-deep));
    -webkit-background-clip: text; background-clip: text; color: transparent;
  }
  .title-line--top { top: 58px; font-size: 124px; letter-spacing: 2px; }
  .title-line--middle { top: 225px; font-size: 96px; letter-spacing: 1px; }
  .title-line--bottom { top: 323px; font-size: 124px; letter-spacing: 2px; }
  .hero-art { position: absolute; left: 25px; top: 561px; width: 680px; height: 460px; }
  .subtitle {
    position: absolute; left: 373px - 0px; top: 688px; width: 0; 
  }
  .tagline {
    position: absolute; left: 258px; top: 686px; width: 230px;
    text-align: center; text-transform: uppercase;
    font-size: 31px; line-height: 31px; letter-spacing: -1.2px;
    color: var(--gold-light);
  }
  .author-plate {
    position: absolute; left: 111px; top: 1037px; width: 506px; height: 66px;
    border: 3px solid var(--gold-deep);
    display: flex; align-items: center; justify-content: center;
    font-size: 29px; color: var(--gold-text); letter-spacing: 0.3px;
  }
</style>
</head>
<body>
<div class="canvas">
  <main class="cover">
    <div class="title-disc"></div>
    <h1 class="title">
      <span class="title-line title-line--top">Nobody</span>
      <span class="title-line title-line--middle">Writes My</span>
      <span class="title-line title-line--bottom">Ending</span>
    </h1>

    <svg class="hero-art" viewBox="0 0 680 460" role="img" aria-label="Purple boxing glove punching through torn white paper">
      <defs>
        <radialGradient id="tearShade" cx="50%" cy="50%" r="55%">
          <stop offset="0" stop-color="#d9d9d9"/>
          <stop offset="1" stop-color="#ffffff" stop-opacity="0"/>
        </radialGradient>
        <linearGradient id="gloveTone" x1="0" y1="0" x2="1" y2="0">
          <stop offset="0" stop-color="var(--glove-light)"/>
          <stop offset="0.55" stop-color="var(--glove-deep)"/>
          <stop offset="0.85" stop-color="var(--glove-light)"/>
          <stop offset="1" stop-color="var(--glove-deep)"/>
        </linearGradient>
      </defs>
      <ellipse cx="345" cy="230" rx="340" ry="225" fill="url(#tearShade)"/>
      <rect x="108" y="72" width="420" height="302" rx="120" fill="url(#gloveTone)"/>
    </svg>

    <p class="tagline">Life<br>Lessons<br>From<br>A 3X Teal<br>Lantern<br>Warrior</p>

    <div class="author-plate">Rae Donnelly, CCMS, MCVP, CSP</div>
  </main>
</div>
</body>
</html>
```